" Atendimento personalizado as necessidades do cliente em todos os ramos de tradução. Assistência 24h com plataforma online. Garantindo a segurança de toda documentação pela QTR, Pex, Velkor. "

```html
<!DOCTYPE html>
<html lang="pt-BR">
<head>
<meta charset="UTF-8">
<title>Veltris Traduções – Cartão de Visita</title>
<link rel="stylesheet" href="https://fonts.googleapis.com/css2?family=Cinzel:wght@700&family=Quicksand:wght@400;500;600&display=swap">
<style>
  :root {
    --backdrop: #e6e8eb;
    --card-navy: #1f3656;
    --card-navy-deep: #1a2e4b;
    --edge-sky: #7cc6f0;
    --accent-sky: #8fd0f5;
    --text-white: #ffffff;
    --text-soft: #c9d6e6;
    --decor-faint: rgba(143, 208, 245, 0.07);
  }
  * { margin: 0; padding: 0; box-sizing: border-box; }
  html, body { width: 1200px; height: 1200px; overflow: hidden; }
  body {
    background: var(--backdrop);
    display: flex;
    flex-direction: column;
    align-items: center;
    justify-content: center;
    gap: 60px;
    font-family: "Quicksand", sans-serif;
  }
  .card {
    position: relative;
    width: 880px;
    height: 490px;
    background: var(--card-navy);
    border-bottom: 10px solid var(--edge-sky);
    border-radius: 4px;
    overflow: hidden;
    box-shadow: 0 14px 30px rgba(20, 30, 50, 0.25);
  }

  /* Front face */
  .card--front {
    display: flex;
    flex-direction: column;
    align-items: center;
    justify-content: center;
  }
  .brand-dot {
    width: 62px;
    height: 62px;
    border-radius: 50%;
    background: var(--accent-sky);
    margin-bottom: 22px;
  }
  .brand-name {
    font-family: "Cinzel", serif;
    font-weight: 700;
    font-size: 92px;
    letter-spacing: 4px;
    color: var(--text-white);
    line-height: 1;
  }
  .brand-tagline {
    margin-top: 14px;
    font-family: "Quicksand", sans-serif;
    font-weight: 500;
    font-size: 26px;
    letter-spacing: 20px;
    padding-left: 20px;
    color: var(--accent-sky);
  }

  /* Back face */
  .card--back { background: var(--card-navy-deep); }
  .back-decor {
    position: absolute;
    left: -90px;
    top: 110px;
    width: 380px;
    height: 380px;
    border-radius: 50%;
    background: var(--decor-faint);
  }
  .holder {
    position: absolute;
    left: 330px;
    top: 70px;
    text-align: right;
    width: 480px;
  }
  .holder-name {
    font-size: 40px;
    font-weight: 500;
    color: var(--text-white);
  }
  .holder-role {
    margin-top: 6px;
    font-size: 17px;
    letter-spacing: 3px;
    color: var(--text-soft);
  }
  .contact-list {
    position: absolute;
    left: 420px;
    top: 210px;
    list-style: none;
    display: flex;
    flex-direction: column;
    gap: 20px;
  }
  .contact-item {
    display: flex;
    align-items: center;
    gap: 16px;
    font-size: 21px;
    color: var(--text-white);
  }
  .contact-icon {
    width: 34px;
    height: 34px;
    flex: none;
  }
  .contact-lines { line-height: 1.35; }
</style>
</head>
<body>

  <section class="card card--front" aria-label="Frente do cartão">
    <div class="brand-dot"></div>
    <h1 class="brand-name">VELTRIS</h1>
    <p class="brand-tagline">TRADUÇÕES</p>
  </section>

  <section class="card card--back" aria-label="Verso do cartão">
    <div class="back-decor"></div>
    <div class="holder">
      <p class="holder-name">Seu Nome e Sobrenome</p>
      <p class="holder-role">CARGO | FUNÇÃO</p>
    </div>
    <ul class="contact-list">
      <li class="contact-item">
        <svg class="contact-icon" viewBox="0 0 34 34" aria-hidden="true">
          <circle cx="17" cy="17" r="17" fill="var(--accent-sky)"/>
          <path d="M12 9.5l3 .2 1.3 4-2 1.5a10 10 0 0 0 4.5 4.5l1.5-2 4 1.3.2 3c-.2 1-1 1.5-2 1.5A14 14 0 0 1 10.5 11.5c0-1 .5-1.8 1.5-2z" fill="var(--card-navy-deep)"/>
        </svg>
        <span>99 9 9999 99 99 | 9999 99 99</span>
      </li>
      <li class="contact-item">
        <svg class="contact-icon" viewBox="0 0 34 34" aria-hidden="true">
          <circle cx="17" cy="17" r="17" fill="var(--accent-sky)"/>
          <rect x="9" y="11" width="16" height="12" rx="1.5" fill="var(--card-navy-deep)"/>
          <path d="M9.5 11.8l7.5 6 7.5-6" fill="none" stroke="var(--accent-sky)" stroke-width="1.6"/>
        </svg>
        <span>contato@veltris.com.br</span>
      </li>
      <li class="contact-item">
        <svg class="contact-icon" viewBox="0 0 34 34" aria-hidden="true">
          <circle cx="17" cy="17" r="17" fill="var(--accent-sky)"/>
          <path d="M17 8a6 6 0 0 0-6 6c0 4.5 6 11.5 6 11.5s6-7 6-11.5a6 6 0 0 0-6-6z" fill="var(--card-navy-deep)"/>
          <circle cx="17" cy="14" r="2.2" fill="var(--accent-sky)"/>
        </svg>
        <span class="contact-lines">Rua Veltris, 9999 | Centro<br>Cidade - UF - CEP: 55.555-555</span>
      </li>
      <li class="contact-item">
        <svg class="contact-icon" viewBox="0 0 34 34" aria-hidden="true">
          <circle cx="17" cy="17" r="17" fill="var(--accent-sky)"/>
          <circle cx="17" cy="17" r="8" fill="none" stroke="var(--card-navy-deep)" stroke-width="2"/>
          <path d="M9 17h16M17 9c-3 3-3 13 0 16M17 9c3 3 3 13 0 16" fill="none" stroke="var(--card-navy-deep)" stroke-width="1.6"/>
        </svg>
        <span>www.veltris.com.br</span>
      </li>
    </ul>
  </section>

</body>
</html>
```